Sample site of what the customer is looking for:
www.tressivocars.example - he doesn't like the girl in the background

- Looking for something easy to navigate, simple, yet different like Tressivo Cars

- For the background image, he's looking for a dusky night scene with a car or a road or something like that

- Accent color - match the logo which is attached unless a different color works better with the design

- Phone number: 555-014-7263

- The buttons for the menu will be: Home, Inventory, About Us & Contact Us

- No content on the homepage

```html
<!DOCTYPE html>
<html lang="en">
<head>
<meta charset="utf-8">
<title>Corvane Auto Collective</title>
<link rel="stylesheet" href="https://fonts.googleapis.com/css2?family=Cabin:wght@400;500;600;700&family=Open+Sans:wght@300&family=Crimson+Text:wght@400&display=swap">
<style>
  :root {
    --navy: #1f3461;
    --accent-red: #8e1d2c;
    --white: #ffffff;
    --ink: #1a1a1a;
    --header-glass: rgba(30, 32, 30, 0.55);
    --footer-black: #050505;
  }
  * { margin: 0; padding: 0; box-sizing: border-box; }
  html, body { width: 1200px; height: 821px; overflow: hidden; background: #222; }
  .page { position: relative; width: 1200px; height: 821px; overflow: hidden; font-family: "Cabin", sans-serif; color: var(--white); }

  .hero-photo {
    position: absolute; inset: 0;
    background:
      linear-gradient(180deg, rgba(0,0,0,0) 55%, rgba(20,20,22,0.85) 100%),
      radial-gradient(ellipse 28% 18% at 72% 62%, #7a1a18 0%, rgba(122,26,24,0) 100%),
      radial-gradient(ellipse 40% 30% at 20% 30%, #6f6a4c 0%, rgba(111,106,76,0) 100%),
      linear-gradient(180deg, #2d3a2c 0%, #3c4a35 45%, #3a3f38 65%, #2a2c2c 100%);
  }

  .top-bar { position: absolute; left: 0; top: 0; width: 1200px; height: 72px; background: var(--header-glass); }

  .brand {
    position: absolute; left: 65px; top: 0; width: 233px; height: 201px;
    background: #f5f5f5; border-top: 6px solid var(--accent-red);
    display: flex; flex-direction: column; align-items: center; justify-content: center;
    font-family: "Crimson Text", serif; color: var(--ink); font-size: 33px; line-height: 1.05; text-align: center;
  }

  .main-nav { position: absolute; top: 28px; left: 0; font-size: 15.5px; font-weight: 500; letter-spacing: -0.2px; }
  .main-nav a { position: absolute; color: var(--white); text-decoration: none; white-space: nowrap; }
  .main-nav .current::after { content: ""; position: absolute; left: -2px; right: -2px; top: 41px; height: 4px; background: var(--accent-red); }

  .search-tab { position: absolute; left: 1147px; top: 8px; width: 53px; height: 53px; }

  .slider-arrow { position: absolute; top: 408px; width: 37px; height: 37px; }
  .headline {
    position: absolute; left: 0; width: 1200px; top: 394px; text-align: center;
    font-family: "Open Sans", sans-serif; font-weight: 300; font-size: 50px; letter-spacing: -0.5px;
    text-shadow: 0 1px 3px rgba(0,0,0,0.4);
  }
  .subline {
    position: absolute; left: 0; width: 1200px; top: 448px; text-align: center;
    font-family: "Open Sans", sans-serif; font-weight: 300; font-size: 25px; letter-spacing: -1px;
  }
  .slider-dots { position: absolute; left: 560px; top: 498px; }

  .cta {
    position: absolute; left: 441px; top: 552px; width: 318px; height: 48px;
    background: var(--navy); color: var(--white); border-radius: 2px;
    display: flex; align-items: center; justify-content: center;
    font-size: 23px; font-weight: 600; letter-spacing: -0.4px; text-decoration: none;
  }

  .footer-bar { position: absolute; left: 0; top: 777px; width: 1200px; height: 44px; background: var(--footer-black); }
  .footer-nav { position: absolute; left: 30px; top: 790px; font-size: 16px; font-weight: 500; letter-spacing: -0.3px; white-space: nowrap; }
  .footer-nav a { color: var(--white); text-decoration: none; }
  .footer-nav .sep { margin: 0 12px; }
  .call-box {
    position: absolute; left: 963px; top: 772px; width: 237px; height: 49px; background: var(--navy);
    font-size: 15.5px; font-weight: 500; letter-spacing: -0.3px; padding: 15px 0 0 13px; white-space: nowrap;
  }
  .call-box .phone { margin-left: 5px; }
</style>
</head>
<body>
<div class="page">
  <div class="hero-photo" role="img" aria-label="Red sports car on a forest road lined with tall pine trees at dusk"></div>

  <div class="top-bar"></div>

  <div class="brand"><span>Corvane</span><span>Auto</span><span>Collective</span></div>

  <nav class="main-nav">
    <a class="current" href="#" style="left:424px">HOME</a>
    <a href="#" style="left:495px">INVENTORY</a>
    <a href="#" style="left:603px">ABOUT US</a>
    <a href="#" style="left:700px">COMMING SOON!</a>
    <a href="#" style="left:856px">CONTACT US</a>
  </nav>

  <svg class="search-tab" viewBox="0 0 53 53" aria-label="Search">
    <polygon points="3,0 53,0 53,53 0,45" fill="#f4f4f4"/>
    <circle cx="24" cy="20" r="7.5" fill="none" stroke="#222" stroke-width="2.6"/>
    <line x1="29.5" y1="25.5" x2="37" y2="33" stroke="#222" stroke-width="3.6" stroke-linecap="round"/>
  </svg>

  <svg class="slider-arrow" style="left:73px" viewBox="0 0 37 37" aria-label="Previous slide">
    <circle cx="18.5" cy="18.5" r="17" fill="none" stroke="#fff" stroke-width="2"/>
    <polyline points="21,12 15,18.5 21,25" fill="none" stroke="#fff" stroke-width="2.2"/>
  </svg>
  <svg class="slider-arrow" style="left:1090px" viewBox="0 0 37 37" aria-label="Next slide">
    <circle cx="18.5" cy="18.5" r="17" fill="none" stroke="#fff" stroke-width="2"/>
    <polyline points="16,12 22,18.5 16,25" fill="none" stroke="#fff" stroke-width="2.2"/>
  </svg>

  <h1 class="headline">Performance, Style &amp; Safety is Our Power</h1>
  <p class="subline">We Build Something AMAZING!!</p>

  <svg class="slider-dots" width="84" height="24" viewBox="0 0 84 24" aria-hidden="true">
    <circle cx="10" cy="12" r="2.5" fill="#fff"/>
    <circle cx="42" cy="12" r="10" fill="none" stroke="#fff" stroke-width="1.8"/>
    <circle cx="42" cy="12" r="2.5" fill="#fff"/>
    <circle cx="72" cy="12" r="2.5" fill="#fff"/>
  </svg>

  <a class="cta" href="#">MORE COMMING SOON!</a>

  <div class="footer-bar"></div>
  <nav class="footer-nav">
    <a href="#">HOME</a><span class="sep">|</span><a href="#">INVENTORY</a><span class="sep">|</span><a href="#">ABOUT US</a><span class="sep">|</span><a href="#">COMMING SOON!</a><span class="sep">|</span><a href="#">CONTACT US</a>
  </nav>
  <div class="call-box">CALL US NOW <span class="phone">555-014-7263</span></div>
</div>
</body>
</html>
```